Corrowin Sack operates across the US and Australasia providing calico bags to small business through to large enterprise across all verticals. Our bags are the most premium in the market place and our customer service is second to none. Our competitive advantage lays in our competitive pricing, superior quality and outstanding customer service.

Industry/Entity Type

Business

Contact Information for Business Card

Corrowin Sack
Marisol Quenby
Managing Director
marisol@corrowinsack.com
www.corrowinsack.com.au
Mobile:- 0471 896 305
Level 3, 284 Harwick Street
Melbourne Victoria Australia 3000

```html
<!DOCTYPE html>
<html lang="en">
<head>
<meta charset="utf-8">
<title>Corrowin Sack – Business Card</title>
<link rel="stylesheet" href="https://fonts.googleapis.com/css2?family=Bodoni+Moda:wght@600&family=Arimo:wght@400&display=swap">
<style>
  :root {
    --page-bg: #e6e6e6;
    --card-white: #ffffff;
    --brand-green: #6cbb48;
    --name-green: #4f8f35;
    --accent-red: #d2232a;
    --map-dark: #4f8a1e;
    --map-light: #b9e29a;
    --ink: #111111;
    --logo-ink: #1a1a1a;
  }
  * { margin: 0; padding: 0; box-sizing: border-box; }
  html, body {
    width: 1189px; height: 1200px; overflow: hidden;
    background: var(--page-bg);
  }
  .card {
    position: absolute; left: 123px;
    width: 943px; height: 539px;
    background: var(--card-white);
    overflow: hidden;
  }
  .card--front { top: 33px; }
  .card--back { top: 627px; }

  .card__wave { position: absolute; left: 0; top: 0; width: 943px; height: 539px; }

  .holder-name {
    position: absolute; left: 55px; top: 66px;
    font-family: "Bodoni Moda", "Didot", serif;
    font-weight: 600; font-size: 52px; line-height: 1;
    color: var(--name-green);
  }
  .holder-title {
    position: absolute; left: 55px; top: 128px;
    font-family: "Arimo", Arial, sans-serif;
    font-size: 28px; line-height: 1; color: var(--ink);
  }

  .brand-mark {
    position: absolute;
    display: flex; align-items: center; justify-content: center;
    border-radius: 38% 44% 40% 46% / 40% 36% 48% 44%;
    background: linear-gradient(135deg, var(--map-dark) 0%, var(--brand-green) 55%, var(--map-light) 100%);
  }
  .brand-mark--front { left: 574px; top: 34px; width: 308px; height: 256px; }
  .brand-mark--back { left: 276px; top: 98px; width: 388px; height: 345px; }
  .brand-name {
    font-family: "Bodoni Moda", "Didot", serif;
    font-weight: 600; color: var(--logo-ink);
    white-space: nowrap;
  }
  .brand-mark--front .brand-name { font-size: 30px; }
  .brand-mark--back .brand-name { font-size: 38px; }

  .contact-list {
    position: absolute; left: 42px; top: 384px;
    list-style: none;
    font-family: "Arimo", Arial, sans-serif;
    font-size: 24px; color: var(--ink);
  }
  .contact-list__item {
    display: flex; align-items: center;
    height: 33.5px;
  }
  .contact-list__icon {
    width: 19px; height: 19px; margin-right: 21px; flex: none;
  }
</style>
</head>
<body>

<section class="card card--front">
  <svg class="card__wave" viewBox="0 0 943 539" aria-hidden="true">
    <path d="M0 292 C180 258 380 300 560 326 C720 346 860 320 943 292 L943 539 L0 539 Z" fill="var(--brand-green)"/>
    <path d="M0 292 C180 258 380 300 560 326 C720 346 860 320 943 292" fill="none" stroke="var(--accent-red)" stroke-width="4"/>
  </svg>

  <h1 class="holder-name">Marisol Quenby</h1>
  <p class="holder-title">Managing Director</p>

  <div class="brand-mark brand-mark--front" role="img" aria-label="Green map of Australia carrying the Corrowin Sack logo">
    <span class="brand-name">Corrowin Sack</span>
  </div>

  <ul class="contact-list">
    <li class="contact-list__item">
      <svg class="contact-list__icon" viewBox="0 0 20 20" aria-hidden="true">
        <rect width="20" height="20" fill="var(--accent-red)"/>
        <path d="M6 4 L8.5 4 L9.5 7 L8 8.3 C8.8 10 10 11.2 11.7 12 L13 10.5 L16 11.5 L16 14 C16 15 15 16 14 16 C9 16 4 11 4 6 C4 5 5 4 6 4 Z" fill="#fff"/>
      </svg>
      <span>0471 896 305</span>
    </li>
    <li class="contact-list__item">
      <svg class="contact-list__icon" viewBox="0 0 20 20" aria-hidden="true">
        <rect width="20" height="20" fill="var(--accent-red)"/>
        <circle cx="10" cy="10" r="5.5" fill="none" stroke="#fff" stroke-width="1.6"/>
        <path d="M4.5 10 H15.5 M10 4.5 C7.5 7 7.5 13 10 15.5 M10 4.5 C12.5 7 12.5 13 10 15.5" fill="none" stroke="#fff" stroke-width="1.2"/>
      </svg>
      <span>marisol@corrowinsack.com</span>
    </li>
    <li class="contact-list__item">
      <svg class="contact-list__icon" viewBox="0 0 20 20" aria-hidden="true">
        <rect width="20" height="20" fill="var(--accent-red)"/>
        <rect x="4" y="6" width="12" height="8" fill="#fff"/>
        <path d="M4 6 L10 10.5 L16 6" fill="none" stroke="var(--accent-red)" stroke-width="1.2"/>
      </svg>
      <span>www.corrowinsack.com.au</span>
    </li>
    <li class="contact-list__item">
      <svg class="contact-list__icon" viewBox="0 0 20 20" aria-hidden="true">
        <rect width="20" height="20" fill="var(--accent-red)"/>
        <path d="M10 16 C7 12 6 10.5 6 8.5 A4 4 0 0 1 14 8.5 C14 10.5 13 12 10 16 Z" fill="#fff"/>
        <circle cx="10" cy="8.5" r="1.5" fill="var(--accent-red)"/>
      </svg>
      <span>Level 3, 284 Harwick Street Melbourne Victoria Australia 3000</span>
    </li>
  </ul>
</section>

<section class="card card--back">
  <div class="brand-mark brand-mark--back" role="img" aria-label="Green map of Australia carrying the Corrowin Sack logo">
    <span class="brand-name">Corrowin Sack</span>
  </div>
</section>

</body>
</html>
```